Wellmere Talking Therapies Hub

We need a design for magazine advert, ideally high resolution to advertise our counselling centre. we would like this to include a photo of two people talking, as if in a counselling session. See our logo and colour range on our website. www.wtth-brackly.co.uk
The photo should not include cups of coffee, clipboards, desks, people touching. it needs to be two people in armchairs sympathetically listening and looking at each other.
The font type is Great Vibes on the logo. Our design should communicate a centre of excellence delivering high quality, professional services in stylishly furnished surroundings.
Updates

Hello Everyone We have had a number of designs that look quite promising but are missing the brief. Can I reiterate that we need a photograph of 2 people seated talking to each other in a sincere way. There shouldn't be office chairs but comfortable chairs. There should be no physical contact. There should be no clipboards.Thank you very muchHeather Added Sunday, March 12, 2017

Target Market(s)

people seeking counselling and psychotherapy

Font styles to use
Other font styles liked:
• Great Vibes as in our logo for some of the print. See attached file.

Requirements
Must have
• good photograph
• Two high res Pixelmarsh photos:
• https://pixelmarsh-files.example-dl.net/attach/get?id=QX81mvB7kTzRwe%2F9PoLnA4Hy%2BdS2cUfjGh0ZrtVbNq6xKe5MsiWoYp3LaDf8TgHu%2BjEw7Rc1Xn%3D%3D
• https://pixelmarsh-files.example-dl.net/attach/get?id=QX81mvB7kTzRwe%2F9PoLnB5Jz%2BeT3dVgkHi1AsuWcOr7yLf6NtjXpZq4MbEg9UhIv%2BkFx8Sd2Yo%3D%3D
Nice to have
• Watermark in keeping with our logo.
Should not have
• Darkness

```html
<!DOCTYPE html>
<html lang="en">
<head>
<meta charset="utf-8">
<title>Wellmere Talking Therapies Hub – Advert</title>
<link href="https://fonts.googleapis.com/css2?family=Great+Vibes&family=Libre+Franklin:wght@400;500&family=Oswald:wght@500&display=swap" rel="stylesheet">
<style>
  :root {
    --ink: #161616;
    --white: #ffffff;
    --leaf-light: #e9f3c4;
    --leaf-mid: #b7d86a;
    --leaf-bright: #9fcb3c;
    --leaf-deep: #6d8f3a;
    --oval-top: #7e9a62;
    --oval-bottom: #3f5e35;
    --oval-rim: #c9d6b4;
    --photo-green: #a8cf52;
    --photo-shirt: #d8e3f0;
    --photo-lilac: #c7b4d6;
  }
  * { margin: 0; padding: 0; box-sizing: border-box; }
  html, body { width: 849px; height: 1200px; overflow: hidden; background: var(--white); }
  .advert {
    position: relative;
    width: 849px;
    height: 1200px;
    overflow: hidden;
    font-family: "Libre Franklin", Arial, sans-serif;
    color: var(--ink);
    background:
      radial-gradient(ellipse 70% 22% at 40% 100%, var(--leaf-bright) 0%, rgba(159,203,60,0) 100%),
      linear-gradient(180deg, var(--white) 0%, var(--white) 56%, var(--leaf-light) 72%, var(--leaf-mid) 88%, var(--leaf-bright) 100%);
  }
  .session-photo {
    position: absolute;
    left: 0; top: 0;
    width: 849px; height: 546px;
    background:
      radial-gradient(ellipse 28% 60% at 18% 70%, var(--photo-lilac) 0%, rgba(199,180,214,0) 100%),
      radial-gradient(ellipse 30% 55% at 68% 65%, var(--photo-shirt) 0%, rgba(216,227,240,0) 100%),
      linear-gradient(135deg, #c8e07a 0%, var(--photo-green) 45%, #8fbf45 75%, #d9ecb0 100%);
  }
  .quote {
    position: absolute;
    left: 0; top: 577px;
    width: 849px;
    text-align: center;
    font-size: 25px;
    line-height: 36px;
  }
  .quote-author {
    position: absolute;
    left: 0; top: 652px;
    width: 849px;
    text-align: center;
    font-size: 18px;
    font-weight: 500;
  }
  .headline {
    position: absolute;
    left: 0; top: 698px;
    width: 849px;
    text-align: center;
    font-family: "Great Vibes", cursive;
    font-weight: 400;
    font-size: 58px;
    line-height: 58px;
  }
  .intro {
    position: absolute;
    left: 0; top: 857px;
    width: 849px;
    text-align: center;
    font-size: 17.5px;
    line-height: 26px;
  }
  .availability {
    position: absolute;
    left: 431px; top: 918px;
    width: 388px; height: 171px;
  }
  .availability svg { position: absolute; left: 0; top: 0; }
  .availability-text {
    position: absolute;
    left: 0; top: 47px;
    width: 388px;
    text-align: center;
    font-family: "Oswald", "Arial Narrow", sans-serif;
    font-weight: 500;
    font-size: 22px;
    line-height: 33px;
    letter-spacing: 0.3px;
    color: var(--white);
  }
  .brand-name {
    position: absolute;
    left: 30px; top: 1090px;
    width: 400px;
    text-align: center;
    font-family: "Great Vibes", cursive;
    font-size: 40px;
    line-height: 42px;
    color: var(--ink);
  }
  .contact {
    position: absolute;
    left: 463px; top: 1122px;
    font-size: 14px;
    line-height: 19px;
    font-weight: 500;
    list-style: none;
  }
</style>
</head>
<body>
  <main class="advert">
    <div class="session-photo" role="img" aria-label="Photograph of two men seated facing each other in a counselling session, one listening and holding a notepad, against a soft green background"></div>

    <p class="quote">“A big part of letting go is recognising when it is time to<br>stay in a situation and when it is time to move on.”</p>
    <p class="quote-author">Marcus T. Ellery</p>

    <h1 class="headline">Confidential Therepeutic Services<br>in the Heart of Millbrook</h1>

    <p class="intro">We have over 30 carefully selected, qualified and professional therapists<br>offering a range of services to help individuals, families and couples.</p>

    <div class="availability">
      <svg width="388" height="171" viewBox="0 0 388 171" aria-hidden="true">
        <defs>
          <linearGradient id="ovalFill" x1="0" y1="0" x2="0" y2="1">
            <stop offset="0" stop-color="var(--oval-top)"/>
            <stop offset="1" stop-color="var(--oval-bottom)"/>
          </linearGradient>
        </defs>
        <ellipse cx="194" cy="86" rx="192" ry="83" fill="var(--oval-rim)"/>
        <ellipse cx="194" cy="85" rx="188" ry="80" fill="url(#ovalFill)"/>
      </svg>
      <p class="availability-text">APPOINTMENTS AVAILABLE<br>THROUGHOUT THE DAY<br>AND EVENING</p>
    </div>

    <p class="brand-name">Wellmere Talking<br>Therapies Hub</p>

    <ul class="contact">
      <li>01632 960418</li>
      <li>www.wtth-brackly.co.uk</li>
      <li>17 Fenwick Road, Millbrook, Brackly BR2 7QD</li>
    </ul>
  </main>
</body>
</html>
```